Design for Certificate

Design a certificate for training, providing our company logo such as attachments. Company's name is "ØSTRA Velmark Advisory Ltd", please refer to our company profile: https://www.ostra-velmark.example/company_info

The style of the current certificate is also attached, and another certificate of another company can be referred to. Psd & jpg are required for the final draft (the layers of psd are not merged). Thanks!

```html
<!DOCTYPE html>
<html lang="en">
<head>
<meta charset="utf-8">
<title>Certificate of Completion – ØSTRA Velmark Advisory Ltd</title>
<link rel="stylesheet" href="https://fonts.googleapis.com/css2?family=Alegreya+Sans:wght@400;500;700;800&display=swap">
<style>
  :root {
    --charcoal: #373a3b;
    --paper: #ffffff;
    --ink: #2e3132;
    --tan: #e2bd9d;
    --gold-light: #f3d99a;
    --gold-pale: #f4ead6;
    --gold-deep: #c4832a;
    --gold-mid: #e6b56e;
  }
  html, body {
    margin: 0;
    padding: 0;
    width: 1200px;
    height: 860px;
    overflow: hidden;
    background: var(--paper);
  }
  .certificate {
    position: relative;
    width: 1200px;
    height: 860px;
    font-family: "Alegreya Sans", sans-serif;
    color: var(--ink);
  }
  .certificate__frame {
    position: absolute;
    inset: 0;
    width: 1200px;
    height: 860px;
  }
  .certificate__title {
    position: absolute;
    left: 68px;
    top: 52px;
    margin: 0;
    font-size: 66px;
    font-weight: 700;
    line-height: 1;
    letter-spacing: 0.5px;
    background: linear-gradient(90deg, var(--gold-mid) 0%, var(--gold-light) 35%, var(--gold-pale) 58%, #d9ad6c 78%, var(--gold-deep) 100%);
    -webkit-background-clip: text;
    background-clip: text;
    color: transparent;
  }
  .cert-number {
    position: absolute;
    left: 878px;
    top: 38px;
    width: 279px;
  }
  .cert-number__label {
    display: block;
    text-align: center;
    color: var(--paper);
    font-size: 21px;
    font-weight: 700;
    line-height: 1;
    padding-left: 14px;
  }
  .cert-number__field {
    display: block;
    margin-top: 10px;
    height: 26px;
    background: var(--paper);
  }
  .text-line {
    position: absolute;
    margin: 0;
    line-height: 1;
    white-space: nowrap;
  }
  .awarded-to { left: 241px; top: 210px; font-size: 28px; letter-spacing: 0.6px; }
  .rule { position: absolute; height: 1px; background: var(--ink); }
  .rule--name { left: 127px; top: 330px; width: 645px; }
  .completed { left: 339px; top: 347px; font-size: 19px; letter-spacing: 0.6px; }
  .course-name { left: 221px; top: 412px; font-size: 47px; font-weight: 700; color: var(--tan); letter-spacing: 0.3px; }
  .course-type { left: 421px; top: 462px; font-size: 34px; letter-spacing: 0.6px; }
  .duration { left: 299px; top: 571px; font-size: 28px; letter-spacing: 0.6px; }
  .rule--date { left: 582px; top: 588px; width: 421px; }
  .issuer { left: 420px; top: 727px; font-size: 40px; font-weight: 800; color: var(--ink); }
  .rule--signature { left: 758px; top: 758px; width: 325px; }
  .signatory { left: 758px; top: 767px; width: 325px; text-align: center; font-size: 21px; letter-spacing: 0.5px; }
  .brand-name {
    position: absolute;
    margin: 0;
    line-height: 1;
    color: var(--tan);
    font-weight: 700;
    white-space: nowrap;
  }
  .brand-name--panel { left: 952px; top: 238px; width: 152px; text-align: center; font-size: 38px; }
  .brand-name--corner { left: 54px; top: 720px; font-size: 62px; }
</style>
</head>
<body>
<main class="certificate">
  <svg class="certificate__frame" viewBox="0 0 2268 1626" aria-hidden="true">
    <defs>
      <linearGradient id="gold-band" x1="0" y1="0" x2="1" y2="0">
        <stop offset="0" stop-color="#ebc27a"/>
        <stop offset="0.22" stop-color="#f1d591"/>
        <stop offset="0.42" stop-color="#f4ead6"/>
        <stop offset="0.6" stop-color="#dcae6e"/>
        <stop offset="0.75" stop-color="#c4832a"/>
        <stop offset="1" stop-color="#ecc388"/>
      </linearGradient>
    </defs>
    <rect class="panel-dark" x="37" y="37" width="2195" height="1551" fill="var(--charcoal)"/>
    <path class="band-gold" fill="url(#gold-band)"
      d="M37,37 H1522 C1560,400 1680,700 1850,950 C2000,1180 2150,1400 2232,1588 H680 C560,1300 400,1000 250,750 C150,560 80,400 37,290 Z"/>
    <path class="field-white" fill="var(--paper)"
      d="M60,287 H1540 C1610,560 1700,780 1830,980 C1980,1200 2120,1400 2200,1565 H695 C580,1290 420,1010 270,760 C170,580 100,420 60,300 Z"/>
    <path class="header-dark" fill="var(--charcoal)"
      d="M60,60 H1498 C1510,140 1524,215 1540,287 H60 Z"/>
  </svg>

  <h1 class="certificate__title">Certificate of Completion</h1>

  <div class="cert-number">
    <span class="cert-number__label">Certificate №</span>
    <span class="cert-number__field"></span>
  </div>

  <p class="brand-name brand-name--panel">ØSTRA</p>

  <p class="text-line awarded-to">This certificate is awarded to</p>
  <span class="rule rule--name"></span>
  <p class="text-line completed" style="width:226px;text-align:center;left:339px;">has successfully completed</p>

  <p class="text-line course-name">Brand Reputation Management</p>
  <p class="text-line course-type">Training Course</p>

  <p class="text-line duration">Sixteen hours, held on</p>
  <span class="rule rule--date"></span>

  <p class="text-line issuer">ØSTRA Velmark</p>
  <span class="rule rule--signature"></span>
  <p class="text-line signatory">Chief Technology Officer</p>

  <p class="brand-name brand-name--corner">ØSTRA</p>
</main>
</body>
</html>
```